Insert card for anti-slip sticker

Product packaging should be inspired by the following
packaging and stand out at the same time: https://shopr.example/7QvKtwe

The packaging is not packaging in the conventional sense, but rather a kind of insert card that can be opened.
This can also be found in the linked product.

On the front of the card: Product name (20 anti-slip strips), advantages of the product and a appealing picture with the product

Inside: Instructions for use and product tips

Back: Images with possible uses, company headquarters, email for contact purposes, note about positive evaluation on Vendaro

```html
<!DOCTYPE html>
<html lang="en">
<head>
<meta charset="utf-8">
<title>20 Anti-slip Strips – Insert Card</title>
<link href="https://fonts.googleapis.com/css2?family=Oswald:wght@600&family=Questrial&family=Arimo:wght@400;700&display=swap" rel="stylesheet">
<style>
  :root {
    --backdrop: #e9e6e1;
    --card: #050505;
    --gold-light: #f3d98a;
    --gold: #c9a24a;
    --gold-dark: #7a5a1c;
    --white: #ffffff;
    --copy-gold: #c79a3c;
    --photo-a: #8c8c8c;
    --photo-b: #3a3a3a;
  }
  * { margin: 0; padding: 0; box-sizing: border-box; }
  html, body { width: 1200px; height: 907px; overflow: hidden; background: var(--backdrop); }
  .card {
    position: absolute; left: 294px; top: 57px;
    width: 612px; height: 792px;
    background: var(--card);
    color: var(--white);
    font-family: "Arimo", Arial, sans-serif;
    overflow: hidden;
  }
  .usage-photo { position: absolute; }
  .usage-label {
    position: absolute;
    font-family: "Questrial", Arial, sans-serif;
    font-size: 16px; letter-spacing: 0.5px;
  }
  .usage-label b { font-weight: 700; font-family: "Arimo", Arial, sans-serif; }
  .title-count {
    position: absolute; left: 320px; top: 86px;
    font-family: "Oswald", sans-serif; font-size: 58px; line-height: 1;
    background: linear-gradient(180deg, var(--gold-light) 0%, var(--gold) 55%, var(--gold-dark) 100%);
    -webkit-background-clip: text; background-clip: text; color: transparent;
  }
  .title-rule { position: absolute; left: 402px; top: 90px; width: 1px; height: 78px; background: var(--white); }
  .title-name {
    position: absolute; left: 410px; top: 94px;
    font-family: "Questrial", Arial, sans-serif; font-size: 38px; line-height: 1; letter-spacing: 1px;
  }
  .title-sub {
    position: absolute; left: 412px; top: 136px;
    font-family: "Questrial", Arial, sans-serif; font-size: 22px; line-height: 1;
  }
  .gold-band {
    position: absolute; height: 9px;
    background: linear-gradient(90deg, var(--gold-dark), var(--gold-light) 45%, var(--gold) 70%, var(--gold-dark));
  }
  .hero-photo {
    position: absolute; left: 306px; top: 204px; width: 306px; height: 326px;
    background: linear-gradient(160deg, #3b3b3b 0%, #6b5a44 45%, #b48a58 75%, #8a6a45 100%);
  }
  .advantages-heading { position: absolute; left: 306px; top: 532px; }
  .advantages-heading span {
    position: absolute; left: 12px; top: 8px;
    font-family: "Oswald", sans-serif; font-size: 19px; line-height: 26px; color: #fff6dc;
    text-transform: uppercase; letter-spacing: 0.3px;
  }
  .advantages-copy {
    position: absolute; left: 328px; top: 617px; width: 262px;
    font-size: 11px; line-height: 14.6px; text-align: justify;
  }
  .back-copy {
    position: absolute; left: 19px; top: 609px; width: 263px;
    font-size: 8.6px; line-height: 11.6px; text-align: justify; color: var(--copy-gold);
  }
  .contact-line {
    position: absolute; left: 0; width: 300px; text-align: center;
    font-size: 11px;
  }
  .web-pill {
    position: absolute; left: 416px; top: 742px; width: 196px; height: 26px;
    border-radius: 13px 0 0 13px;
    background: linear-gradient(90deg, var(--gold-dark), var(--gold) 50%, #5a3f12);
    font-family: "Questrial", Arial, sans-serif; font-size: 14px; letter-spacing: 2px;
    line-height: 26px; text-align: center;
  }
</style>
</head>
<body>
<main class="card">
  <svg class="usage-photo" style="left:0;top:34px" width="282" height="98" viewBox="0 0 282 98" role="img" aria-label="Photo: person in boots climbing stairs fitted with dark anti-slip strips">
    <defs><linearGradient id="stairs" x1="0" y1="0" x2="1" y2="1"><stop offset="0" stop-color="#b8b8b8"/><stop offset="1" stop-color="#555"/></linearGradient></defs>
    <polygon points="1,1 245,1 280,97 1,97" fill="url(#stairs)" stroke="var(--gold)" stroke-width="2"/>
  </svg>
  <p class="usage-label" style="left:20px;top:145px"><b>Anti-slip</b> Strips</p>

  <svg class="usage-photo" style="left:18px;top:209px" width="288" height="100" viewBox="0 0 288 100" role="img" aria-label="Photo: bare feet standing on a dark anti-slip mat on a boat deck">
    <defs><linearGradient id="deck" x1="0" y1="0" x2="0" y2="1"><stop offset="0" stop-color="#9aa3ad"/><stop offset="1" stop-color="#2e2e2e"/></linearGradient></defs>
    <polygon points="28,1 287,1 287,99 1,99" fill="url(#deck)" stroke="var(--gold)" stroke-width="2"/>
  </svg>
  <p class="usage-label" style="left:162px;top:318px"><b>Anti-slip</b> Strips</p>

  <svg class="usage-photo" style="left:0;top:374px" width="282" height="96" viewBox="0 0 282 96" role="img" aria-label="Photo: wooden stair treads covered with grey anti-slip pads">
    <defs><linearGradient id="treads" x1="0" y1="0" x2="1" y2="1"><stop offset="0" stop-color="#e8e2d8"/><stop offset="0.5" stop-color="#9a7a52"/><stop offset="1" stop-color="#4a4a4a"/></linearGradient></defs>
    <polygon points="1,1 258,1 280,95 1,95" fill="url(#treads)" stroke="var(--gold)" stroke-width="2"/>
  </svg>
  <p class="usage-label" style="left:20px;top:485px"><b>Anti-slip</b> Strips</p>

  <div class="title-count">20</div>
  <div class="title-rule"></div>
  <h1 class="title-name">Anti-slip</h1>
  <p class="title-sub">Strips</p>

  <div class="gold-band" style="left:306px;top:195px;width:306px"></div>
  <div class="hero-photo" role="img" aria-label="Photo: person in sneakers stepping onto clear anti-slip strips on a wooden floor at a doorway"></div>
  <div class="gold-band" style="left:306px;top:524px;width:306px"></div>

  <svg class="advantages-heading" width="192" height="66" viewBox="0 0 192 66" aria-hidden="true">
    <defs><linearGradient id="plate" x1="0" y1="0" x2="1" y2="1"><stop offset="0" stop-color="#f0d48a"/><stop offset="0.5" stop-color="#b98c3a"/><stop offset="1" stop-color="#6e4f18"/></linearGradient></defs>
    <polygon points="0,0 192,0 176,66 0,66" fill="url(#plate)"/>
  </svg>
  <h2 class="advantages-heading" style="width:192px;height:66px"><span>Advantages of<br>the product</span></h2>

  <p class="advantages-copy">advantages of the product &nbsp;advantages of the product advantages of the product &nbsp;advantages of the product advantages of the product advantages of the product advantages of the product &nbsp;advantages of the product advantages of the product advantages of the product</p>

  <p class="back-copy">advantages of the product &nbsp;dvantages of the product advantages of the product advantages of the product advantages of the product advantages of the product advantages of the product advantages of the product advantages of the product advantages of the product</p>

  <p class="contact-line" style="top:695px;left:2px">Company Headquarters</p>
  <p class="contact-line" style="top:724px">Email</p>
  <p class="contact-line" style="top:766px">note about positive evaluation on Vendaro</p>

  <div class="web-pill">www.stridegrip.example</div>
</main>
</body>
</html>
```